Business Card Design. For a portrait and wedding photography business

Silver Willow Studio Weddings, Portraits, Bar/Bat Mitzvah, Sweet 16's, On the Cutting Edge of Digital Photography Corporate Events High Quality Photography at an Affordable PricesCustom Wedding Packages.Custom Designed Album, Thank you cardsExpert Photo Editing and Retouching

Target Market(s)

Families for family portraits, head shots for business cards,, wedding clients, Suite 16's, bar/bat mitzvah, parties, and corporate events,
.

Industry/Entity Type

Wedding

Contact Information for Business Card

Daniel K. Fenwick 47 Larchmere Lane Maplecrest, N.Y. 14306 By Appointment Only

Font styles to use
Script
Other font styles liked:
• Time New Romen

Requirements
Must have
• I would like to use one of the photograph I uploaded I would prefer to let the designer choose based on their expertise.
Nice to have
• Leave it up to the designer
Should not have
• The card should not be too dark

```html
<!DOCTYPE html>
<html lang="en">
<head>
<meta charset="utf-8">
<title>Silver Willow Studio — Business Card</title>
<link rel="stylesheet" href="https://fonts.googleapis.com/css2?family=Pinyon+Script&family=Open+Sans:wght@400&display=swap">
<style>
  :root {
    --backdrop: #e9e4dc;
    --card: #ffffff;
    --ink: #111111;
    --bracket: #0d0d0d;
    --photo-dark: #1f2b22;
    --photo-mid: #4d5a55;
    --photo-stone: #8a8f90;
    --overlay-text: #ffffff;
  }
  * { margin: 0; padding: 0; box-sizing: border-box; }
  html, body {
    width: 1200px; height: 1000px; overflow: hidden;
    background: var(--backdrop);
  }
  .canvas { position: relative; width: 1200px; height: 1000px; }

  .card {
    position: absolute;
    width: 504px; height: 861px;
    box-shadow: 0 6px 18px rgba(0,0,0,0.18);
  }
  .card--info {
    left: 76px; top: 69px;
    background: var(--card);
    color: var(--ink);
    text-align: center;
    font-family: "Open Sans", Arial, sans-serif;
  }
  .card__brackets { position: absolute; inset: 0; }

  .studio-name {
    position: absolute; left: 0; right: 0; top: 100px;
    font-family: "Pinyon Script", cursive;
    font-weight: 400;
    font-size: 52px; line-height: 62px;
  }
  .services {
    position: absolute; left: 0; right: 0; top: 245px;
    list-style: none;
    font-size: 15.5px; line-height: 26.3px;
  }
  .photographer {
    position: absolute; left: 0; right: 0; top: 430px;
  }
  .photographer__name {
    font-family: "Pinyon Script", cursive;
    font-size: 35px; line-height: 42px; font-weight: 400;
  }
  .photographer__role { font-size: 20px; line-height: 26px; }

  .contact {
    position: absolute; left: 0; right: 0; top: 552px;
    font-size: 24px; line-height: 34px;
  }
  .address {
    position: absolute; left: 0; right: 0; top: 692px;
    font-style: normal;
    font-size: 20px; line-height: 28px;
  }

  .card--photo {
    left: 629px; top: 67px;
    overflow: hidden;
  }
  .card__photo {
    position: absolute; inset: 0;
    background: linear-gradient(90deg, var(--photo-dark) 0%, #2c3a30 35%, var(--photo-mid) 55%, var(--photo-stone) 75%, #6d7274 100%);
  }
  .card__photo::after {
    content: ""; position: absolute; left: 0; right: 0; bottom: 0; height: 300px;
    background: linear-gradient(180deg, rgba(40,48,60,0) 0%, rgba(44,52,66,0.85) 100%);
  }
  .card__web {
    position: absolute; left: 18px; top: 16px;
    color: var(--overlay-text);
    font-family: "Open Sans", Arial, sans-serif;
    font-size: 21px;
  }
</style>
</head>
<body>
<div class="canvas">

  <section class="card card--info">
    <svg class="card__brackets" width="504" height="861" viewBox="0 0 504 861" aria-hidden="true">
      <g fill="none" stroke="var(--bracket)" stroke-width="5">
        <path d="M23.5 93 V28.5 H86"/>
        <path d="M419 28.5 H481.5 V93"/>
        <path d="M23.5 769 V835.5 H86"/>
        <path d="M419 835.5 H481.5 V769"/>
      </g>
    </svg>

    <h1 class="studio-name">Silver Willow<br>Studio</h1>

    <ul class="services">
      <li>Weddings, Portraits, Bar/Bat Mitzvah, Sweet 16's</li>
      <li>On the Cutting Edge of Digital Photography Corporate Events</li>
      <li>High Quality Photography at an Affordable Prices</li>
      <li>Custom Wedding Packages</li>
      <li>Custom Designed Album, Thank you cards</li>
      <li>Expert Photo Editing and Retouching</li>
    </ul>

    <div class="photographer">
      <p class="photographer__name">Daniel K. Fenwick</p>
      <p class="photographer__role">Photographer</p>
    </div>

    <div class="contact">
      <p>555-201-0172</p>
      <p>www.silverwillowstudio.com</p>
    </div>

    <address class="address">
      47 Larchmere Lane Maplecrest<br>
      N.Y. 14306<br>
      By Appointment Only
    </address>
  </section>

  <section class="card card--photo">
    <div class="card__photo" role="img" aria-label="Wedding photograph: bride and groom embracing beside a stone archway, with trees and greenery behind them"></div>
    <p class="card__web">www.silverwillowstudio.com</p>
  </section>

</div>
</body>
</html>
```